Dynamic Business Card for Sports Supplements Company

Hi! I'm looking for an awesome business card to match my existing sports supplement company. I have uploaded my current company logo and screenshot of the front page of my website.

I would like to have something dynamic and interesting and utilize the colors in the website - the reds and purples

The business card should be double sided and focus on a unique eye-catching design on the back and include all the relevant company info.

Most importantly, it should say somewhere: "Sign up on our website for a coupon code."

Target Market(s)

Mostly for women gym goers but it shouldn't be too feminine. It should be in keeping with the website design. It should flow and clearly be connected to it

Industry/Entity Type

Business

Contact Information for Business Card

Lorena K. Vasquez
CEO
LVasquez@Fortivanco.example
www.fortivanco.example
614.275.3081
P.O. Box 48317
Burke, Virginia 22417

Sign up on our website for a coupon code

Font styles to use
Serif
Sans Serif
Other font styles liked:
• Novecento font family and "Fortivan" is in AR Destine font

Requirements
Must have
• One side should be a bold Fortivan logo design. Even just the symbol itself may be o.k. (see attached file)

```html
<!DOCTYPE html>
<html lang="en">
<head>
<meta charset="utf-8">
<title>Fortivan — Business Card Front</title>
<link rel="stylesheet" href="https://fonts.googleapis.com/css2?family=Audiowide&display=swap">
<style>
  :root {
    --card-black: #000000;
    --brand-red: #ec1c24;
    --brand-purple: #662d91;
    --brand-white: #ffffff;
  }
  html, body {
    margin: 0;
    padding: 0;
    width: 1200px;
    height: 687px;
    overflow: hidden;
    background: var(--card-black);
  }
  .card {
    position: relative;
    width: 1200px;
    height: 687px;
    background: var(--card-black);
    overflow: hidden;
  }
  .card__diagonal {
    position: absolute;
    inset: 0;
    width: 1200px;
    height: 687px;
  }
  .card__diagonal .stripe { fill: var(--brand-purple); }
  .card__diagonal .corner { fill: var(--brand-red); }
  .brand-mark {
    position: absolute;
    left: 516px;
    top: 170px;
    width: 160px;
    height: 160px;
    background: var(--brand-red);
  }
  .brand-name {
    position: absolute;
    left: 0;
    width: 1192px;
    top: 440px;
    margin: 0;
    text-align: center;
    font-family: "Audiowide", sans-serif;
    font-weight: 400;
    font-size: 84px;
    line-height: 1;
    letter-spacing: 6px;
    text-transform: uppercase;
    color: var(--brand-white);
  }
</style>
</head>
<body>
  <main class="card">
    <svg class="card__diagonal" viewBox="0 0 1200 687" aria-hidden="true">
      <polygon class="stripe" points="1162,0 1200,0 1200,0 635,687 600,687"/>
      <polygon class="corner" points="1193,0 1200,0 1200,687 635,687"/>
    </svg>
    <div class="brand-mark" aria-hidden="true"></div>
    <h1 class="brand-name">Fortivan</h1>
  </main>
</body>
</html>
```